Brindle's Custom Signs and Woodworking Business Card

I run a small business that does custom woodworking and sign making. I have a logo already that I am very fond of, and would like to continue with the theme of the logo. I'd like a business card that adds onto that theme/design and stands out among typical business cards. As you'll be able to see from the logo, we're a patriotic brand and that is paramount to us.
Contact Information for Business Card
beneath the Brindle's logo, I'd like it to say
"Custom Signs & Woodworking"
Also, I'd like the following information template present on the card, preferably with the logos of instagram and facebook present besides the title.
(Name)                                 (Instragram)
(Email)                                  (Facebook)
(Phone)                                 (Website)
I would like for the name, email, and phone number to be editable so that I can have my employees utilize this card design as well. but for my card, my information is as follows
Dan "Brindle" Korvell, CEO                                           @BrindlesCustoms
Dan@BrindlesCustoms.example                                          Brindle's Customs
(555) 274-6103                                                         BrindlesCustoms.example
As for the back side, either a full american flag, or something that catches the eye, designer's preference I suppose.
Font styles to use
Other font styles liked:
- Funkydori, an adobe typekit font. it is the same as used for the logo. I'm not sure how the whole card will look with that, so if it doesn't look right please use something that complements the script style of the logo

```html
<!DOCTYPE html>
<html lang="en">
<head>
<meta charset="utf-8">
<title>Brindle's Custom Signs and Woodworking – Business Card</title>
<link rel="stylesheet" href="https://fonts.googleapis.com/css2?family=Arimo:ital,wght@0,700;1,700&family=Lora:ital,wght@1,700&display=swap">
<style>
  :root {
    --navy: #1c2a6e;
    --red: #c0172f;
    --white: #ffffff;
    --paper: #f4f5f7;
    --stage: #2e2e30;
  }
  * { box-sizing: border-box; margin: 0; padding: 0; }
  html, body { width: 1200px; height: 900px; overflow: hidden; }
  body {
    background: var(--stage);
    font-family: "Arimo", Arial, sans-serif;
    position: relative;
  }
  .card {
    position: absolute;
    top: 140px;
    width: 360px;
    height: 620px;
    border-radius: 30px;
    overflow: hidden;
  }

  /* back side: stars-and-stripes field built from plain bands */
  .card-back {
    left: 200px;
    background: repeating-linear-gradient(
      to bottom,
      var(--red) 0 24px,
      var(--white) 24px 48px
    );
  }
  .back-band {
    position: absolute;
    left: 0; right: 0;
    background: var(--navy);
  }
  .back-band.top { top: 0; height: 96px; }
  .back-band.bottom { bottom: 0; height: 96px; }
  .back-panel {
    position: absolute;
    left: 34px; right: 34px;
    top: 230px;
    height: 160px;
    border-radius: 22px;
    background: var(--navy);
    border: 6px solid var(--white);
    display: flex;
    align-items: center;
    justify-content: center;
  }
  .back-wordmark {
    font-weight: 700;
    font-size: 60px;
    color: var(--white);
    letter-spacing: 1px;
  }

  /* front side */
  .card-front {
    left: 620px;
    background: var(--paper);
    padding: 58px 0 0 46px;
  }
  .brand {
    display: flex;
    align-items: center;
    gap: 12px;
  }
  .brand-mark {
    width: 22px; height: 22px;
    border-radius: 50%;
    background: var(--red);
  }
  .brand-name {
    font-weight: 700;
    font-size: 50px;
    color: var(--navy);
    line-height: 1;
  }
  .tagline {
    font-family: "Lora", Georgia, serif;
    font-style: italic;
    font-weight: 700;
    color: var(--navy);
    font-size: 21px;
    line-height: 1.1;
    margin: 14px 0 0 96px;
  }
  .tagline .amp { font-size: 16px; }
  .person { margin-top: 118px; }
  .person-name {
    font-style: italic;
    font-weight: 700;
    font-size: 19px;
    color: var(--navy);
  }
  .person-title {
    font-weight: 700;
    font-size: 14px;
    color: var(--red);
    margin-top: 2px;
  }
  .contacts { list-style: none; margin-top: 16px; }
  .contacts li {
    display: flex;
    align-items: center;
    gap: 8px;
    font-weight: 700;
    font-size: 16px;
    color: var(--navy);
    line-height: 24px;
  }
  .contacts li.gap { margin-top: 14px; }
  .icon { width: 13px; height: 13px; flex: none; }
  .dot {
    width: 12px; height: 12px; flex: none;
    border-radius: 50%;
    background: var(--red);
  }
  .website {
    margin-top: 16px;
    font-weight: 700;
    font-size: 17px;
    color: var(--red);
  }
</style>
</head>
<body>

  <section class="card card-back" aria-label="Card back">
    <div class="back-band top"></div>
    <div class="back-panel">
      <span class="back-wordmark">Brindle's</span>
    </div>
    <div class="back-band bottom"></div>
  </section>

  <section class="card card-front" aria-label="Card front">
    <div class="brand">
      <span class="brand-mark"></span>
      <span class="brand-name">Brindle's</span>
    </div>
    <p class="tagline">Custom Signs<br><span class="amp">&amp;</span> Woodworking</p>

    <div class="person">
      <p class="person-name">Dan "Brindle" Korvell</p>
      <p class="person-title">Chief Executive Officer</p>
    </div>

    <ul class="contacts">
      <li>
        <svg class="icon" viewBox="0 0 16 16" aria-hidden="true">
          <circle cx="8" cy="8" r="7" fill="none" stroke="var(--red)" stroke-width="1.6"/>
          <path d="M5.2 4.6 l1.4-.3 .8 1.8 -.9.7 c.5 1 1.2 1.7 2.2 2.2 l.7-.9 1.8.8 -.3 1.4 c-3.2 0-5.7-2.5-5.7-5.7z" fill="var(--red)"/>
        </svg>
        (555) 274-6103
      </li>
      <li>
        <svg class="icon" viewBox="0 0 16 16" aria-hidden="true">
          <circle cx="8" cy="8" r="7" fill="var(--red)"/>
          <rect x="4" y="5.2" width="8" height="5.6" fill="none" stroke="var(--white)" stroke-width="1.1"/>
          <path d="M4 5.4 L8 8.5 L12 5.4" fill="none" stroke="var(--white)" stroke-width="1.1"/>
        </svg>
        Dan@BrindlesCustoms.example
      </li>
      <li class="gap"><span class="dot"></span>@BrindlesCustoms</li>
      <li><span class="dot"></span>Brindle's Customs</li>
    </ul>

    <p class="website">www.BrindlesCustoms.example</p>
  </section>

</body>
</html>
```